Yearbook of one of our programs

Our company, Meridian Ascent, www.meridianascent.example, hosts leadership programs and workshops for women in leadership roles from different companies all around the world. We need a year book, 11 x 17 inches, we will print with a soft cover, and be approximately 70 pages. Due date for the final completion is 12/9. However, the initial contest & fee is only for pages 1-5, 26-27 and 40-41 (please see attached last year's version). We’d like to use the same color as that. Also attached is the outline we will use once a designer is selected. $50 hourly rate for the completion of the book is set once a designer is confirmed.

```html
<!DOCTYPE html>
<html lang="en">
<head>
<meta charset="utf-8">
<title>Ascent Circle Yearbook – Pages 02–03</title>
<link rel="stylesheet" href="https://fonts.googleapis.com/css2?family=Dancing+Script:wght@700&family=Open+Sans:wght@300;400;600&display=swap">
<style>
  :root {
    --crimson: #a3295a;
    --crimson-deep: #8c2248;
    --crimson-bright: #c2396c;
    --slate: #444b5e;
    --paper: #eef0f6;
    --ink: #2f3342;
    --ink-soft: #4a4e5c;
    --white: #ffffff;
    --backdrop: #d9dbe2;
  }
  * { box-sizing: border-box; margin: 0; padding: 0; }
  html, body { width: 1200px; height: 789px; overflow: hidden; background: var(--backdrop); }
  .spread { position: relative; width: 1200px; height: 789px; display: flex; font-family: "Open Sans", sans-serif; }
  .page { position: relative; width: 600px; height: 789px; overflow: hidden; }

  /* Left page */
  .page--photo { background: linear-gradient(135deg, var(--crimson-deep) 0%, var(--crimson) 55%, var(--crimson-bright) 100%); }
  .edge-strip { position: absolute; left: 0; width: 14px; }
  .edge-strip--light { top: 330px; height: 70px; background: var(--paper); }
  .edge-strip--pink { top: 400px; height: 240px; background: var(--crimson-bright); }
  .photo-frame { position: absolute; left: 108px; top: 150px; width: 400px; height: 420px; background: rgba(255,255,255,0.35); padding: 14px; }
  .photo-fill { width: 100%; height: 100%; background: linear-gradient(160deg, #e9dccc 0%, #a28e7d 40%, #4a3a36 75%, #2c2428 100%); }
  .sq { position: absolute; }
  .sq--white { left: 82px; top: 168px; width: 62px; height: 62px; background: var(--paper); box-shadow: 0 0 0 6px var(--crimson-bright); }
  .sq--glass-top { left: 250px; top: 140px; width: 60px; height: 60px; background: rgba(255,255,255,0.45); }
  .sq--glass-bottom { left: 440px; top: 470px; width: 80px; height: 70px; background: rgba(255,255,255,0.35); }
  .sq--dark-bottom { left: 480px; top: 540px; width: 40px; height: 40px; background: rgba(68,75,94,0.55); }
  .sq--tr-pink { left: 540px; top: 155px; width: 26px; height: 26px; background: var(--crimson-bright); }
  .sq--tr-white { left: 558px; top: 150px; width: 12px; height: 12px; border: 4px solid var(--white); border-left: none; border-bottom: none; }
  .sq--mid-pink { left: 540px; top: 215px; width: 16px; height: 16px; background: rgba(255,255,255,0.3); }
  .sq--bl-pink { left: 130px; top: 580px; width: 26px; height: 26px; background: var(--crimson-bright); }
  .sq--bl-slate { left: 148px; top: 574px; width: 12px; height: 12px; border: 4px solid var(--slate); border-left: none; border-bottom: none; }
  .sq--foot-glass { left: 440px; top: 680px; width: 24px; height: 24px; background: rgba(255,255,255,0.35); }
  .sq--foot-pink { left: 456px; top: 672px; width: 14px; height: 14px; background: var(--crimson-bright); }

  .folio { position: absolute; bottom: 28px; font-size: 11px; letter-spacing: 0.5px; text-transform: uppercase; }
  .folio span { margin: 0 6px; opacity: 0.7; }
  .folio::after { content: ""; position: absolute; left: -20px; right: -20px; bottom: -16px; height: 8px; background: var(--slate); }
  .folio--left { right: 40px; color: var(--white); }
  .folio--right { left: 40px; color: var(--crimson); }

  /* Right page */
  .page--letter { background: var(--paper); }
  .top-bar { position: absolute; left: 20px; top: 0; width: 110px; height: 8px; background: var(--slate); }
  .letter { position: absolute; left: 40px; top: 30px; width: 500px; color: var(--ink-soft); }
  .letter__title { font-family: "Dancing Script", cursive; font-weight: 700; font-size: 26px; color: var(--crimson); margin-bottom: 20px; }
  .letter__greeting { font-size: 13px; color: var(--ink); margin-bottom: 16px; }
  .letter__lead { font-size: 13px; font-weight: 600; color: var(--ink); line-height: 1.5; margin-bottom: 14px; }
  .letter p.body { font-size: 12.5px; font-weight: 300; line-height: 1.5; margin-bottom: 12px; }
  .highlight-band { position: absolute; left: 0; top: 478px; width: 440px; height: 20px; background: var(--crimson); color: var(--white); font-size: 11.5px; line-height: 20px; text-align: right; padding-right: 12px; }
  .letter__closing { position: absolute; left: 40px; top: 620px; font-size: 14px; color: var(--ink); }
  .signature { position: absolute; left: 40px; top: 650px; width: 120px; height: 44px; background: linear-gradient(90deg, rgba(47,51,66,0.25), rgba(47,51,66,0.08)); border-radius: 4px; }
  .sq--r-pink { left: 520px; top: 150px; width: 26px; height: 26px; background: var(--crimson-bright); }
  .sq--r-slate { left: 534px; top: 142px; width: 18px; height: 18px; background: var(--slate); z-index: -1; }
  .r-bar { position: absolute; bottom: 0; width: 12px; }
  .r-bar--pink { right: 22px; height: 170px; background: var(--crimson-bright); }
  .r-bar--slate { right: 36px; height: 110px; background: var(--slate); }
  .sq--rb-grey { left: 470px; top: 712px; width: 22px; height: 22px; background: #cfd1db; }
  .sq--rb-pink { left: 484px; top: 702px; width: 16px; height: 16px; background: var(--crimson-bright); }
</style>
</head>
<body>
<main class="spread">
  <section class="page page--photo">
    <div class="edge-strip edge-strip--light"></div>
    <div class="edge-strip edge-strip--pink"></div>
    <div class="photo-frame">
      <div class="photo-fill" role="img" aria-label="Photo of two smiling program members chatting on a sunny porch"></div>
    </div>
    <div class="sq sq--white"></div>
    <div class="sq sq--glass-top"></div>
    <div class="sq sq--glass-bottom"></div>
    <div class="sq sq--dark-bottom"></div>
    <div class="sq sq--tr-pink"></div>
    <div class="sq sq--tr-white"></div>
    <div class="sq sq--mid-pink"></div>
    <div class="sq sq--bl-pink"></div>
    <div class="sq sq--bl-slate"></div>
    <div class="sq sq--foot-glass"></div>
    <div class="sq sq--foot-pink"></div>
    <div class="folio folio--left">Ascent Circle<span>|</span>02</div>
  </section>

  <section class="page page--letter">
    <div class="top-bar"></div>
    <div class="sq sq--r-slate"></div>
    <div class="sq sq--r-pink"></div>
    <article class="letter">
      <h1 class="letter__title">A Heartfelt Thank you</h1>
      <p class="letter__greeting">Ladies,</p>
      <p class="letter__lead">What a year it has been! We put 2020 in our rearview, yet many of the challenges followed us. Despite the continued conditions 2021 presented, we faced them together, and stand stronger and wiser as a result.</p>
      <p class="body">This year, we were able to be back in person with two magnificent Ascent Summits, in Park City, Utah and “down at the farm” near Atlanta, Georgia. And throughout the year, we maintained constant connection through our virtual sessions, small group huddles, and one-on-one connections, which I’ve become quite fond of as well.</p>
      <p class="body">When we gathered in Utah, I opened the session asking us all to think how much “Words Matter.” More than ever, a single expression of support, an open query for help, a small note to share how we are thinking of each other, or suggestions for the “must-have” beauty products… these have helped fuel us along this often rocky, unstable journey.</p>
      <p class="body" style="margin-top:40px">While 2021 has been remarkable in so many ways, the support and joy this group gives to each other is the stand-out. You all are a truly remarkable group. I am personally honored to be a part of your journey. This yearbook is a reminder of the year we’ve had, the wisdom we’ve shared, and the memories we’ve made.</p>
    </article>
    <div class="highlight-band">But the word I offered in Utah to put in front of us was “remarkable.”</div>
    <p class="letter__closing">All the best,</p>
    <div class="signature" role="img" aria-label="Handwritten signature of the program director"></div>
    <div class="sq sq--rb-grey"></div>
    <div class="sq sq--rb-pink"></div>
    <div class="r-bar r-bar--slate"></div>
    <div class="r-bar r-bar--pink"></div>
    <div class="folio folio--right">Ascent Circle<span>|</span>03</div>
  </section>
</main>
</body>
</html>
```